fun theme dental practice website!

This client LOVES their superhero theme! They are an established pediatric dental practice with multiple locations. They have recently expanded to see adults and do orthodontics. They would like to have a new website design for the adult part of their practice. It should be similar in theme (superhero) but more adult (no sugarbugs!) . Navigation: about, meet the team, treatments, orthodontics, contact
add appointment request feature

Target Market(s)

adults

Industry/Entity Type

Dental

Number of Pages Required

2 page

Requirements
Must have
• home page design and interior page design
• fun and in theme but not too babyish (should it still look like a comic book?)
• appointment request feature
• visual pow
• colors consistent with logo (see attached)
• use the tooth social media icons

```html
<!DOCTYPE html>
<html lang="en">
<head>
<meta charset="utf-8">
<title>Meet the team – Valor Dental &amp; Orthodontics</title>
<link href="https://fonts.googleapis.com/css2?family=Montserrat:ital,wght@0,400;0,500;0,600;1,400&display=swap" rel="stylesheet">
<style>
  :root {
    --green: #8cc63f;
    --green-active: #5ea82a;
    --charcoal: #3a3a3a;
    --red: #c8242b;
    --mustard: #c3b41f;
    --text-light: #e6e3df;
    --title: #dedede;
    --footer-bg: #f2f2f2;
    --footer-text: #6a6a6a;
    --photo-warm: #a28c70;
  }
  * { box-sizing: border-box; margin: 0; padding: 0; }
  html, body { width: 1200px; height: 930px; overflow: hidden; }
  body { font-family: "Montserrat", Arial, sans-serif; background: var(--footer-bg); position: relative; }

  .site-header {
    position: relative; z-index: 5;
    height: 75px; background: var(--green);
    display: flex; align-items: center; justify-content: space-between;
    padding: 0 40px 0 40px;
    box-shadow: 0 2px 3px rgba(0,0,0,.25);
  }
  .brand {
    display: flex; align-items: center; gap: 10px;
    font-weight: 600; font-size: 17px; color: #fff; text-decoration: none;
  }
  .brand-mark { width: 18px; height: 18px; border-radius: 50%; background: #fff; }
  .main-nav { display: flex; gap: 40px; }
  .main-nav a {
    color: #fff; text-decoration: none; font-size: 13px; letter-spacing: 1px;
    text-transform: uppercase; font-weight: 500;
  }
  .main-nav a.is-active { color: var(--green-active); }

  .team-page { position: relative; height: 790px; overflow: hidden; }
  .backdrop-circle {
    position: absolute; z-index: 1; pointer-events: none;
    left: 370px; top: -80px; width: 830px; height: 830px; border-radius: 50%;
    background: rgba(255,255,255,.18);
  }
  .page-hero {
    height: 175px; background: var(--charcoal);
    display: flex; align-items: center; justify-content: center;
  }
  .page-title {
    position: relative; z-index: 2;
    font-weight: 500; font-size: 37px; color: var(--title); letter-spacing: .5px;
  }

  .member { height: 205px; position: relative; }
  .member--red { background: var(--red); }
  .member--mustard { background: var(--mustard); }
  .member-inner {
    position: relative; z-index: 2;
    display: flex; gap: 15px; padding: 28px 0 0 104px;
    color: var(--text-light);
  }
  .member--flip .member-inner { flex-direction: row-reverse; padding: 27px 33px 0 118px; text-align: right; }
  .member-photo {
    flex: none; width: 150px; height: 150px; border-radius: 12px;
    background: linear-gradient(150deg, #b7a48a, var(--photo-warm) 55%, #6f5e4a);
  }
  .member-info { padding-top: 11px; font-size: 16px; line-height: 21px; }
  .member-name { font-weight: 600; font-size: 17px; }
  .member-role { font-style: italic; }
  .member-bio { margin-top: 21px; }
  .member-bio a { color: var(--green); }
  .member-info--wide { width: 830px; }
  .member-info--mid { width: 883px; }
  .member-info--narrow { width: 770px; }

  .site-footer {
    height: 65px; background: var(--footer-bg);
    display: flex; align-items: center; justify-content: center;
    font-size: 18px; color: var(--footer-text); letter-spacing: .3px;
  }
</style>
</head>
<body>
  <header class="site-header">
    <a class="brand" href="#"><span class="brand-mark"></span>Valor Dental &amp; Orthodontics</a>
    <nav class="main-nav">
      <a href="#">About</a>
      <a href="#" class="is-active">Meet the team</a>
      <a href="#">Schedule an appointment</a>
      <a href="#">Treatments</a>
      <a href="#">Orthodontics</a>
      <a href="#">Contact</a>
    </nav>
  </header>

  <main class="team-page">
    <div class="backdrop-circle"></div>
    <section class="page-hero">
      <h1 class="page-title">Meet the team</h1>
    </section>

    <article class="member member--red">
      <div class="member-inner">
        <div class="member-photo" role="img" aria-label="Portrait photo of John Doe"></div>
        <div class="member-info member-info--wide">
          <h2 class="member-name">John Doe</h2>
          <p class="member-role">Metus</p>
          <p class="member-bio">Sed vitae massa vitae felis lobortis placerat. Vivamus et hendrerit augue. Donec a tempor enim. <a href="#">Nulla link</a> sollicitudin molestie justo sit amet dictum. Quisque tincidunt sapien eget faucibus egestas metus.</p>
        </div>
      </div>
    </article>

    <article class="member member--mustard member--flip">
      <div class="member-inner">
        <div class="member-photo" role="img" aria-label="Portrait photo of Joanna Joe"></div>
        <div class="member-info member-info--mid">
          <h2 class="member-name">Joanna Joe</h2>
          <p class="member-role">Duis</p>
          <p class="member-bio">Donec vitae sollicitudin justo. Aenean vel magna feugiat erat feugiat vulputate. Nam ultrices sollicitudin dolor, in tempus nibh posuere eget. Morbi semper augue sed aliquam fringilla. Ut turpis duis.</p>
        </div>
      </div>
    </article>

    <article class="member member--red">
      <div class="member-inner">
        <div class="member-photo" role="img" aria-label="Photo of Jordan Dok at work in surgical gear"></div>
        <div class="member-info member-info--narrow">
          <h2 class="member-name">Jordan Dok</h2>
          <p class="member-role">Posuere</p>
          <p class="member-bio">Aenean fringilla dolor quis urna placerat varius. Proin sit amet efficitur urna. Suspendisse tempus risus eu neque tincidunt pretium. Suspendisse tincidunt aliquet arcu. Duis non elit tellus. Vestibulum vel nisi posuere.</p>
        </div>
      </div>
    </article>
  </main>

  <footer class="site-footer">Valor Dental &amp; Orthodontics © 2016</footer>
</body>
</html>
```